Torven Medical needs bold attention catching website for healthcare professionals(target)

I need a hero page as well as a products and about page for a website of mine. I specialize in orthopedic instruments . Specifically bone drills and saws. This whole company was founded to bring superb quality highly discounted medical instruments. Specifically bone drills, bone saws, k-wires and pins. Two main points should be cost savings and superior quality.

Target Market(s)

healthcare professionals Surgeons and hospital material managers

Number of Pages Required

3 page

Font styles to use
Serif

Colors

Designer to choose colors to be used in the design.

Requirements
Must have
• colors should match logo design

```html
<!DOCTYPE html>
<html lang="en">
<head>
<meta charset="utf-8">
<title>Torven Medical — Orthopedic Products</title>
<link href="https://fonts.googleapis.com/css2?family=PT+Serif:wght@400;700&family=Open+Sans:wght@400;600&display=swap" rel="stylesheet">
<style>
:root{
  --orange:#f7901e;
  --ink:#222;
  --muted:#777;
  --page:#f6f8fb;
  --card:#fff;
  --footer:#2d2d2d;
  --white:#fff;
}
*{margin:0;padding:0;box-sizing:border-box}
html,body{width:784px;height:1200px;overflow:hidden}
body{position:relative;background:var(--white);font-family:'Open Sans',sans-serif;color:var(--ink)}
.serif{font-family:'PT Serif',serif}
.abs{position:absolute}

/* header */
.site-header{position:absolute;left:0;top:0;width:784px;height:74px;background:var(--white)}
.brand{left:113px;top:26px;font-family:'PT Serif',serif;font-size:16px;color:var(--ink);letter-spacing:.2px}
.nav{left:282px;top:30px;display:flex;gap:15px;font-family:'PT Serif',serif;font-size:8px}
.nav span{color:var(--ink)}
.nav .active{color:var(--orange)}
.nav .caret{font-size:6px;margin-left:2px}
.search{left:564px;top:25px;width:94px;height:23px;border:1px solid #bbb;border-radius:3px;font-family:'PT Serif',serif;font-size:7.5px;color:#888;padding:6px 8px}
.search svg{position:absolute;right:8px;top:7px}

/* hero */
.hero{left:0;top:74px;width:784px;height:203px;background:radial-gradient(ellipse at 50% 40%,#6f6f72 0%,#505154 55%,#3c3d40 100%)}
.hero-kicker{left:0;top:133px;width:777px;text-align:center;font-family:'PT Serif',serif;font-size:20px;color:var(--orange)}
.hero-title{left:0;top:160px;width:777px;text-align:center;font-family:'PT Serif',serif;font-weight:700;font-size:26px;color:var(--white)}
.hero-text{left:0;top:202px;width:777px;text-align:center;font-size:8px;color:var(--white)}

/* products */
.products{left:0;top:277px;width:784px;height:567px;background:var(--page)}
.card{position:absolute;width:171px;height:195px;background:var(--card)}
.badge{position:absolute;right:9px;top:6px;width:22px;height:22px;border-radius:50%;background:var(--orange);color:var(--white);font-size:7px;line-height:22px;text-align:center}
.photo{position:absolute;left:20px;top:40px;width:131px;height:82px;border-radius:4px;background:radial-gradient(ellipse,#dcdde0 0%,#f2f3f5 60%,#fff 100%)}
.stars{position:absolute;left:0;top:136px;width:171px;text-align:center}
.name{position:absolute;left:0;top:150px;width:171px;text-align:center;font-family:'PT Serif',serif;font-size:10px;color:var(--ink)}
.price{position:absolute;left:0;top:171px;width:171px;text-align:center;font-family:'PT Serif',serif;font-size:10px;color:var(--muted)}

.pager{left:358px;top:765px;display:flex;align-items:center;font-family:'PT Serif',serif;font-size:10px;color:#999}
.pager .current{width:20px;height:20px;background:var(--orange);color:var(--white);text-align:center;line-height:20px;margin-right:14px}
.pager span+span{margin-right:8px}

/* assistance band */
.assist{left:0;top:844px;width:784px;height:132px;background:var(--orange);color:var(--white);text-align:center}
.assist h2{position:absolute;left:0;top:46px;width:777px;font-family:'PT Serif',serif;font-weight:400;font-size:14px}
.assist p{position:absolute;left:0;top:70px;width:777px;font-size:8px}
.assist p b{font-family:'PT Serif',serif;font-size:11.5px;text-decoration:underline;font-weight:700}

/* footer */
.footer{left:0;top:976px;width:784px;height:224px;background:var(--footer);color:var(--white)}
.footer-links{left:0;top:36px;width:784px;display:flex;justify-content:center;font-family:'PT Serif',serif;font-size:10px}
.footer-links span{padding:0 14px;border-left:1px solid var(--orange);line-height:10px}
.footer-links span:first-child{border-left:none}
.footer h3{position:absolute;top:82px;font-family:'PT Serif',serif;font-weight:400;font-size:14px;color:var(--orange)}
.cert{left:113px;top:113px;font-size:7px;line-height:16.6px}
.contact{left:253px;top:113px;font-size:7px;line-height:20.6px}
.contact b{color:var(--orange);font-weight:600}
.contact svg{vertical-align:-1px;margin-right:3px}
.email{left:532px;top:115px;width:126px;height:23px;background:var(--white);border-radius:2px;font-size:7px;color:#999;padding:6px 12px}
.subscribe{left:532px;top:146px;width:63px;height:23px;background:var(--orange);border-radius:2px;font-family:'PT Serif',serif;font-size:7.5px;text-align:center;line-height:23px}
.copyright{left:113px;top:202px;font-size:6.5px}
.legal{left:572px;top:202px;font-size:6.5px}
</style>
</head>
<body>
<svg width="0" height="0" style="position:absolute">
  <defs>
    <symbol id="star" viewBox="0 0 10 10"><polygon points="5,0 6.2,3.6 10,3.6 6.9,5.9 8.1,9.6 5,7.3 1.9,9.6 3.1,5.9 0,3.6 3.8,3.6" fill="#f7901e"/></symbol>
  </defs>
</svg>

<header class="site-header">
  <div class="abs brand">Torven Medical</div>
  <nav class="abs nav">
    <span class="active">Home</span><span>About Us</span><span>Products<span class="caret">&#8964;</span></span><span>Pricing<span class="caret">&#8964;</span></span><span>Contact Us</span>
  </nav>
  <div class="abs search">Search
    <svg width="7" height="7" viewBox="0 0 10 10"><circle cx="4" cy="4" r="3" fill="none" stroke="#666" stroke-width="1.5"/><line x1="6.3" y1="6.3" x2="9" y2="9" stroke="#666" stroke-width="1.5"/></svg>
  </div>
</header>

<section class="abs hero" role="img" aria-label="Surgical scissors and clamps on a grey cloth"></section>
<div class="abs hero-kicker">Our High Quality</div>
<h1 class="abs hero-title">Orthopedic Products</h1>
<p class="abs hero-text">Lorem ipsum dolor sit amet, consectetur adipiscing elit, sed do eiusmod tempor incididunt</p>

<section class="abs products">
  <article class="card" style="left:114px;top:59px">
    <span class="badge">New</span><div class="photo" role="img" aria-label="Bone saw blade"></div>
    <div class="stars"><svg width="48" height="7"><use href="#star" x="0" width="7" height="7"/><use href="#star" x="10" width="7" height="7"/><use href="#star" x="20" width="7" height="7"/><use href="#star" x="30" width="7" height="7"/><use href="#star" x="40" width="7" height="7"/></svg></div>
    <div class="name">Bone Saw</div><div class="price">$320</div>
  </article>
  <article class="card" style="left:300px;top:59px">
    <span class="badge">New</span><div class="photo" role="img" aria-label="Surgical bone drill"></div>
    <div class="stars"><svg width="48" height="7"><use href="#star" x="0" width="7" height="7"/><use href="#star" x="10" width="7" height="7"/><use href="#star" x="20" width="7" height="7"/><use href="#star" x="30" width="7" height="7"/><use href="#star" x="40" width="7" height="7"/></svg></div>
    <div class="name">Bone Drill</div><div class="price">$550</div>
  </article>
  <article class="card" style="left:486px;top:59px">
    <span class="badge">New</span><div class="photo" role="img" aria-label="Set of drill bits"></div>
    <div class="stars"><svg width="48" height="7"><use href="#star" x="0" width="7" height="7"/><use href="#star" x="10" width="7" height="7"/><use href="#star" x="20" width="7" height="7"/><use href="#star" x="30" width="7" height="7"/><use href="#star" x="40" width="7" height="7"/></svg></div>
    <div class="name">Drill Bits</div><div class="price">$150</div>
  </article>
  <article class="card" style="left:114px;top:269px">
    <span class="badge">New</span><div class="photo" role="img" aria-label="Two k-wires crossed"></div>
    <div class="stars"><svg width="48" height="7"><use href="#star" x="0" width="7" height="7"/><use href="#star" x="10" width="7" height="7"/><use href="#star" x="20" width="7" height="7"/><use href="#star" x="30" width="7" height="7"/><use href="#star" x="40" width="7" height="7"/></svg></div>
    <div class="name">Bone Saw</div><div class="price">$320</div>
  </article>
  <article class="card" style="left:300px;top:269px">
    <span class="badge">New</span><div class="photo" role="img" aria-label="Orthopedic pins"></div>
    <div class="stars"><svg width="48" height="7"><use href="#star" x="0" width="7" height="7"/><use href="#star" x="10" width="7" height="7"/><use href="#star" x="20" width="7" height="7"/><use href="#star" x="30" width="7" height="7"/><use href="#star" x="40" width="7" height="7"/></svg></div>
    <div class="name">Pins</div><div class="price">$210</div>
  </article>
  <article class="card" style="left:486px;top:269px">
    <span class="badge">New</span><div class="photo" role="img" aria-label="Holding forceps"></div>
    <div class="stars"><svg width="48" height="7"><use href="#star" x="0" width="7" height="7"/><use href="#star" x="10" width="7" height="7"/><use href="#star" x="20" width="7" height="7"/><use href="#star" x="30" width="7" height="7"/><use href="#star" x="40" width="7" height="7"/></svg></div>
    <div class="name">Holding Forceps</div><div class="price">$50</div>
  </article>
</section>

<nav class="abs pager"><span class="current">1</span><span>2</span><span>3</span><span>4</span></nav>

<section class="abs assist">
  <h2>Need any type of assistance related to our orthopedic instruments ?</h2>
  <p><svg width="7" height="7" viewBox="0 0 10 10"><path d="M2 0.5 L4 2.8 L3 4 Q4.5 6.5 6 7 L7.2 6 L9.5 8 L8 9.6 Q3.5 9 0.4 2 Z" fill="#fff"/></svg> Call Us at <b>+123 555 01987</b></p>
</section>

<footer class="abs footer">
  <div class="abs footer-links"><span>Our Products</span><span>News &amp; Events</span><span>Become a Distributor</span><span>FAQ’s</span><span>Vendor Registartion</span></div>
  <h3 style="left:113px">Certificates</h3>
  <h3 style="left:253px">Get In Touch</h3>
  <h3 style="left:532px">Newsletter</h3>
  <div class="abs cert">ISO : 9001-2015<br>ISO 13485:2016<br>Quality Policy<br>WHO: GMP Compliance</div>
  <div class="abs contact">
    <div><svg width="7" height="7" viewBox="0 0 10 10"><path d="M5 0.5 L10 5 H8.5 V9.5 H6 V6.5 H4 V9.5 H1.5 V5 H0 Z" fill="#f7901e"/></svg><b>Address:</b> 123 Your Street, Your City, United States of America (12345)</div>
    <div><svg width="7" height="7" viewBox="0 0 10 10"><path d="M2 0.5 L4 2.8 L3 4 Q4.5 6.5 6 7 L7.2 6 L9.5 8 L8 9.6 Q3.5 9 0.4 2 Z" fill="#f7901e"/></svg><b>Telephone:</b> +12-34-55501200 (100 lines)</div>
    <div><svg width="7" height="7" viewBox="0 0 10 10"><rect x="0.7" y="2" width="8.6" height="6.4" fill="none" stroke="#f7901e" stroke-width="1.1"/><path d="M0.7 2 L5 5.5 L9.3 2" fill="none" stroke="#f7901e" stroke-width="1.1"/></svg><b>Email:</b> info@torvenmedical.com</div>
  </div>
  <div class="abs email">Enter email here...</div>
  <div class="abs subscribe">Subscribe</div>
  <div class="abs copyright">Copyright © 2019 torvenmedical.com. All rights reserved.</div>
  <div class="abs legal">Disclaimer &nbsp;&nbsp;|&nbsp;&nbsp; Privacy Policy</div>
</footer>
</body>
</html>
```